Buch-/E-Book-Cover für Schriftstellerin
Vielen Dank für das schöne Cover zu meiner Kurzgeschichtensammlung!
Zielgruppe
30-jährige Schriftstellerin (Kurzgeschichten, Roman in Arbeit, Gedichte)
Zielgruppe der Kurzgeschichtensammlung 'Sofawirbel': 17-50 Jährige Kurzgeschichten-Leser (alle Geschlechter), Tomio Sadakawa-, Brackwater-, Lodur-Leser, Hobby-Philosophen, Intellektuelle, Melancholiker
Klappentext:
„Miese Gedanken sind der Isolierstoff zwischen mir und meiner Umwelt.“
Eine Frau geht in ihrer Badewanne an Bord eines Papierschiffs, ein Paar wandert über Möbel und ein Mann, dessen Name sich keiner merken kann, spricht von der Couch aus mit seinen Bücherschränken...
„Sofawirbel“ nähert sich dem modernen Menschen auf einfühlsame wie humoristische Weise. Psychologisch, verträumt, surreal und wohltuend melancholisch - in 14 Kurzgeschichten treffen Personen und Mobiliar, Seelenraum und Außenwelt, Pandemie und Heavy Metal aufeinander.
Aufgabenstellung
Design passend zum Titel 'Sofawirbel'. In meiner Geschichte ist das Sofawirbel der Moment, in dem der depressive und angstgeplagte Protagonist auf der Couch liegt und sich das Chaos vorstellt, das er anrichten würde, wenn er die Möbel auf den Kopf stellen würde, sodass die Schubladen der Schränke keinen Sinn mehr ergäben oder er seinen Körper aufschneiden würde. Die Geschichte hat ein Happy End und er wird gesund. Es ist nur ein kurzer Moment der Depression. Die 14 Kurzgeschichten sind nachenklich, ehrlich, aber auch stellenweise lustig sowie surreal.
Das Cover soll farbenfroh sein und mit serifenloser Schrift, abstrakt-künstlerisch und modern. Bitte keine Fotos von 'realen' Menschen.
Titel: Sofawirbel (kann auch großgeschrieben sein)
Untertitel: 14 Kurzgeschichten
Autorin: Marlene Tieck
Ansonsten keine Vorgaben.

```html
<!DOCTYPE html>
<html lang="de">
<head>
<meta charset="utf-8">
<title>Sofawirbel – Marlene Tieck</title>
<link rel="stylesheet" href="https://fonts.googleapis.com/css2?family=Anton&family=Bebas+Neue&display=swap">
<style>
  :root {
    --bg-top: #d4891a;
    --bg-mid: #e4b040;
    --bg-light: #f5d36a;
    --bg-bottom: #d2b259;
    --ink: #ffffff;
    --cloud-light: #f1ece0;
    --cloud-shade: #cfc6b4;
    --sofa: #c9707f;
    --sofa-dark: #a9566a;
  }
  html, body {
    margin: 0;
    padding: 0;
    overflow: hidden;
    background: var(--bg-mid);
  }
  .cover {
    position: relative;
    width: 750px;
    height: 1200px;
    overflow: hidden;
    background:
      radial-gradient(ellipse 60% 35% at 15% 75%, var(--bg-light) 0%, rgba(245,211,106,0) 70%),
      linear-gradient(180deg, var(--bg-top) 0%, var(--bg-mid) 45%, #e8bd52 65%, var(--bg-bottom) 100%);
  }
  .cloud {
    position: absolute;
    border-radius: 50%;
    background: radial-gradient(ellipse at 45% 40%, var(--cloud-light) 0%, #e4ddcd 55%, rgba(207,198,180,0) 75%);
  }
  .cloud--side {
    left: -60px;
    top: 390px;
    width: 170px;
    height: 200px;
    opacity: 0.85;
  }
  .cloud--main {
    left: 135px;
    top: 570px;
    width: 485px;
    height: 285px;
  }
  .sofa {
    position: absolute;
    left: 77px;
    top: 868px;
    width: 618px;
    height: 200px;
    border-radius: 90px 90px 14px 14px;
    background: linear-gradient(180deg, var(--sofa) 0%, #c46b7b 60%, var(--sofa-dark) 100%);
  }
  .sofa-shadow {
    position: absolute;
    left: 130px;
    top: 1075px;
    width: 500px;
    height: 40px;
    border-radius: 50%;
    background: radial-gradient(ellipse, rgba(140,100,30,0.35) 0%, rgba(140,100,30,0) 70%);
  }
  .type {
    position: absolute;
    inset: 0;
  }
  .author, .subtitle {
    font-family: "Bebas Neue", "Oswald", sans-serif;
    fill: var(--ink);
  }
  .title {
    font-family: "Anton", "Oswald", sans-serif;
    fill: var(--ink);
  }
</style>
</head>
<body>
  <main class="cover">
    <div class="cloud cloud--side" role="img" aria-label="Angeschnittene weiße Wolke am linken Rand"></div>
    <div class="cloud cloud--main" role="img" aria-label="Schwebende weiße Wolke über dem Sofa"></div>
    <div class="sofa-shadow"></div>
    <div class="sofa" role="img" aria-label="Rosafarbenes Samtsofa mit Knopfheftung"></div>

    <svg class="type" width="750" height="1200" viewBox="0 0 750 1200">
      <text class="author" x="375" y="63" font-size="45" text-anchor="middle" textLength="182" lengthAdjust="spacingAndGlyphs">MARLENE TIECK</text>

      <text class="title" x="98" y="290" font-size="233" textLength="400" lengthAdjust="spacingAndGlyphs">SOF</text>
      <g transform="rotate(180 571 188.5)">
        <text class="title" x="571" y="290" font-size="233" text-anchor="middle" textLength="122" lengthAdjust="spacingAndGlyphs">A</text>
      </g>

      <text class="title" x="103" y="498" font-size="233" textLength="532" lengthAdjust="spacingAndGlyphs">WIRBEL</text>

      <text class="subtitle" x="372" y="567" font-size="57" text-anchor="middle" textLength="340" lengthAdjust="spacingAndGlyphs">14 KURZGESCHICHTEN</text>
    </svg>
  </main>
</body>
</html>
```